PRVD Traditional Business Card Project

Please see attached....just a simple business card... on attachment- please use the exact font, style, etc as the attached "Pat Everard Wynne" card... however, replace with the "Owen Reginald Talbot" text and address below the card.

```html
<!DOCTYPE html>
<html lang="en">
<head>
<meta charset="utf-8">
<title>PRVD Business Card – Owen Reginald Talbot</title>
<link rel="stylesheet" href="https://fonts.googleapis.com/css2?family=Libre+Baskerville:wght@700&family=Arimo:wght@400&display=swap">
<style>
  :root {
    --page-bg: #ececec;
    --card-border: #8b8b8b;
    --card-face: #d2d5d2;
    --corner-mark: #f6f6f6;
    --ink: #161616;
    --ink-soft: #2a2a2a;
  }
  html, body {
    margin: 0;
    width: 1200px;
    height: 900px;
    overflow: hidden;
    background: var(--page-bg);
  }
  .canvas {
    width: 1200px;
    height: 900px;
    display: flex;
    align-items: center;
    justify-content: center;
  }
  .card {
    position: relative;
    width: 1050px;
    height: 600px;
    box-sizing: border-box;
    background: var(--card-border);
    padding: 16px;
    box-shadow: 0 6px 18px rgba(0,0,0,0.18);
  }
  .card-face {
    position: relative;
    width: 100%;
    height: 100%;
    background: var(--card-face);
    color: var(--ink);
  }
  .corner-marks {
    position: absolute;
    inset: 0;
    width: 100%;
    height: 100%;
    pointer-events: none;
  }
  .firm {
    position: absolute;
    left: 40px;
    top: 26px;
  }
  .firm-name {
    font-family: "Libre Baskerville", serif;
    font-weight: 700;
    font-variant: small-caps;
    font-size: 38px;
    letter-spacing: 1px;
    line-height: 1;
    margin: 0;
  }
  .firm-type {
    font-family: "Arimo", sans-serif;
    font-size: 14px;
    letter-spacing: 3px;
    text-transform: uppercase;
    color: var(--ink-soft);
    margin: 8px 0 0 0;
  }
  .person {
    position: absolute;
    left: 225px;
    top: 150px;
    text-align: right;
  }
  .person-name {
    font-family: "Libre Baskerville", serif;
    font-weight: 700;
    font-variant: small-caps;
    font-size: 56px;
    letter-spacing: 1px;
    line-height: 1;
    margin: 0;
    white-space: nowrap;
  }
  .person-title {
    font-family: "Arimo", sans-serif;
    font-size: 20px;
    letter-spacing: 9px;
    text-transform: uppercase;
    margin: 10px 0 0 0;
    text-align: center;
    padding-left: 120px;
  }
  .address,
  .contact {
    position: absolute;
    font-family: "Arimo", sans-serif;
    font-size: 21px;
    line-height: 1.3;
    letter-spacing: 1px;
    margin: 0;
  }
  .address {
    left: 40px;
    bottom: 78px;
    text-transform: uppercase;
  }
  .address .web { text-transform: none; }
  .contact {
    left: 640px;
    bottom: 36px;
  }
  .contact .label { text-transform: uppercase; }
</style>
</head>
<body>
<main class="canvas">
  <article class="card">
    <div class="card-face">
      <svg class="corner-marks" viewBox="0 0 1018 568" preserveAspectRatio="none" aria-hidden="true">
        <g fill="none" stroke="var(--corner-mark)" stroke-width="6">
          <polyline points="6,40 6,6 40,6"/>
          <polyline points="978,6 1012,6 1012,40"/>
          <polyline points="6,528 6,562 40,562"/>
          <polyline points="978,562 1012,562 1012,528"/>
        </g>
      </svg>

      <header class="firm">
        <p class="firm-name">Pacific Ridge</p>
        <p class="firm-type">Valley Defense, PLC</p>
      </header>

      <section class="person">
        <h1 class="person-name">Owen Reginald Talbot</h1>
        <p class="person-title">Attorney at Law</p>
      </section>

      <address class="address">
        2740 Alder Court, Suite B<br>
        Fairview Glen, CA 90210<br>
        <span class="web">www.prvdlaw.com</span>
      </address>

      <p class="contact">
        <span class="label">Tel</span> (555) 214-7730<br>
        <span class="label">Fax</span> (555) 214-7731<br>
        otalbot@prvdlaw.com
      </p>
    </div>
  </article>
</main>
</body>
</html>
```